11 x 11 Flyer Design for Social Media - Reverse Mortgages

62 or older?

A Reverse Mortgage
could be
Your Road to Financial Freedom

* No Monthly Payments
* No Income Requirements
* No Credit Score Requirements
* No Loss of Ownership

Receive cash by lump sum, monthly installments or a line of credit!!

Call us today for a Free Consultation!!
(800) 471-2965

Bluegate Financial Services, Inc.
NMLS #318760
www.bluegatehome.com

```html
<!DOCTYPE html>
<html lang="en">
<head>
<meta charset="utf-8">
<title>62 or Older? Reverse Mortgage Flyer</title>
<link href="https://fonts.googleapis.com/css2?family=Bebas+Neue&family=Jost:wght@300;400;500;600;700&display=swap" rel="stylesheet">
<style>
  :root{
    --blue:#0b5c87;
    --blue-dark:#0a4468;
    --green:#9dca3a;
    --white:#ffffff;
    --ink:#1a1a1a;
    --ring:#5f8fab;
  }
  *{margin:0;padding:0;box-sizing:border-box;}
  html,body{width:1200px;height:1109px;overflow:hidden;background:var(--white);}
  .flyer{position:relative;width:1200px;height:1109px;overflow:hidden;font-family:"Jost",sans-serif;background:var(--white);}

  .layer{position:absolute;left:0;top:0;width:1200px;height:1109px;pointer-events:none;}
  .layer *{white-space:nowrap;}

  .brand{position:absolute;left:0;top:0;width:480px;height:200px;background:var(--white);display:flex;align-items:center;gap:14px;padding-left:36px;}
  .brand-dot{width:34px;height:34px;border-radius:50%;background:var(--blue);flex:none;}
  .brand-name{font-size:25px;font-weight:500;color:var(--blue);line-height:1.15;}

  .info-panel{position:absolute;left:0;top:200px;width:480px;height:909px;background:var(--blue);}
  .info-panel .notch{position:absolute;left:211px;top:0;width:0;height:0;border-left:14px solid transparent;border-right:14px solid transparent;border-top:16px solid var(--white);}

  .hero-photo{position:absolute;left:480px;top:0;width:720px;height:598px;
    background:linear-gradient(180deg,#a9c6de 0%,#cfdde8 38%,#b9cdd6 55%,#e9eef0 100%);}

  .age{position:absolute;left:6px;top:238px;font-family:"Bebas Neue",sans-serif;font-size:205px;line-height:1;color:var(--white);letter-spacing:-2px;}
  .or{position:absolute;left:191px;top:246px;font-size:100px;font-weight:500;line-height:1;color:var(--green);}
  .older{position:absolute;left:189px;top:326px;font-size:110px;font-weight:600;line-height:1;color:var(--green);letter-spacing:-1px;text-shadow:6px 5px 0 var(--blue-dark);}

  .rule{position:absolute;left:8px;top:453px;width:300px;height:3px;background:var(--white);}
  .offer{position:absolute;left:8px;top:478px;color:var(--white);}
  .offer-title{font-size:36px;font-weight:700;line-height:1;letter-spacing:0.3px;}
  .offer-sub{font-size:17.5px;font-weight:500;margin-top:6px;letter-spacing:0.2px;}

  .benefits{list-style:none;}
  .benefit-line{position:absolute;left:49px;top:600px;width:3px;height:300px;background:var(--ring);}
  .benefit{position:absolute;left:10px;display:flex;align-items:center;width:460px;}
  .benefit-icon{width:80px;height:80px;border-radius:50%;background:var(--white);border:7px solid var(--ring);display:flex;align-items:center;justify-content:center;flex:none;}
  .benefit-text{margin-left:14px;font-size:20px;font-weight:500;color:var(--white);border-bottom:1.5px dashed #c9d9e4;padding-bottom:4px;}
  .benefit-text .no{color:var(--green);}

  .payout{position:absolute;left:4px;top:961px;width:440px;height:120px;border:2px dashed var(--green);border-radius:12px;padding:8px 0 0 28px;color:var(--green);font-size:28px;font-weight:600;line-height:1.24;}

  .consult-band{position:absolute;left:480px;top:598px;width:720px;height:192px;background:var(--green);}
  .consult-band .notch{position:absolute;left:346px;top:192px;width:0;height:0;border-left:28px solid transparent;border-right:28px solid transparent;border-top:26px solid var(--green);}
  .consult-title{position:absolute;left:480px;top:718px;width:720px;text-align:center;font-size:46px;font-weight:600;color:var(--white);letter-spacing:-0.5px;white-space:nowrap;}

  .gallery-photo{position:absolute;top:497px;width:206px;height:196px;border-radius:50%;border:9px solid var(--white);box-shadow:0 3px 8px rgba(0,0,0,.18);}
  .gallery-photo.one{left:503px;background:linear-gradient(160deg,#b7dcd6,#6b7f87 60%,#d3dde6);}
  .gallery-photo.two{left:734px;background:linear-gradient(160deg,#9fbf8a,#c9b79b 50%,#2d3f55);}
  .gallery-photo.three{left:965px;background:linear-gradient(120deg,#e7dfe3 30%,#a77a52 55%,#a3272e 85%);}

  .phone-icon{position:absolute;left:543px;top:840px;}
  .call-label{position:absolute;left:617px;top:826px;font-size:55px;font-weight:300;color:var(--green);line-height:1;letter-spacing:-0.5px;}
  .call-number{position:absolute;left:620px;top:880px;font-family:"Bebas Neue",sans-serif;font-size:96px;line-height:1;color:var(--ink);letter-spacing:0.5px;}
  .company-line{position:absolute;left:567px;top:972px;display:flex;align-items:center;gap:8px;font-size:21px;line-height:1.2;color:var(--ink);}
  .web-button{position:absolute;left:640px;top:1016px;width:392px;height:65px;background:var(--green);border-radius:4px;display:flex;align-items:center;justify-content:center;gap:12px;color:var(--white);font-size:23px;font-weight:500;letter-spacing:0.5px;}
</style>
</head>
<body>
<main class="flyer">
  <div class="hero-photo" role="img" aria-label="Smiling senior couple in white shirts standing together on a beach by the sea"></div>

  <header class="brand">
    <span class="brand-dot"></span>
    <span class="brand-name">Bluegate Financial<br>Services, Inc.</span>
  </header>

  <section class="info-panel"><span class="notch"></span></section>

  <h1 class="layer headline">
    <span class="age">62</span>
    <span class="or">OR</span>
    <span class="older">OLDER?</span>
  </h1>

  <div class="layer">
    <div class="rule"></div>
    <div class="offer">
      <h2 class="offer-title">A REVERSE MORTGAGE</h2>
      <p class="offer-sub">COULD BE YOUR ROAD TO FINANCIAL FREEDOM</p>
    </div>
    <div class="benefit-line"></div>
  </div>

  <ul class="layer benefits">
    <li class="benefit" style="top:557px">
      <span class="benefit-icon">
        <svg width="44" height="36" viewBox="0 0 44 36" fill="none" stroke="#1e8fd6" stroke-width="2.2" stroke-linejoin="round"><rect x="12" y="3" width="29" height="19" rx="2"/><line x1="12" y1="9" x2="41" y2="9"/><path d="M3 24 L14 17 L24 18 L18 23 L26 23 L30 28 L12 32 L3 30 Z"/></svg>
      </span>
      <span class="benefit-text"><span class="no">No</span> Monthly Payments</span>
    </li>
    <li class="benefit" style="top:656px">
      <span class="benefit-icon">
        <svg width="44" height="38" viewBox="0 0 44 38" fill="none" stroke="#1e8fd6" stroke-width="2.2" stroke-linejoin="round"><circle cx="30" cy="11" r="9"/><path d="M33 7 h-4 a2 2 0 0 0 0 4 h2 a2 2 0 0 1 0 4 h-4 M30 5 v2 M30 15 v2"/><path d="M3 26 L12 21 L22 22 L17 27 L25 27 L36 22 L38 25 L26 34 L12 34 L3 32 Z"/></svg>
      </span>
      <span class="benefit-text"><span class="no">No</span> Income Requirements</span>
    </li>
    <li class="benefit" style="top:759px">
      <span class="benefit-icon">
        <svg width="44" height="36" viewBox="0 0 44 36" fill="none" stroke="#1e8fd6" stroke-width="2.2" stroke-linejoin="round"><rect x="9" y="3" width="30" height="20" rx="2" transform="rotate(-10 24 13)"/><rect x="5" y="11" width="32" height="21" rx="2" fill="#fff"/><line x1="5" y1="17" x2="37" y2="17"/><line x1="10" y1="25" x2="20" y2="25"/></svg>
      </span>
      <span class="benefit-text"><span class="no">No</span> Credit Score Requirements</span>
    </li>
    <li class="benefit" style="top:862px">
      <span class="benefit-icon">
        <svg width="44" height="40" viewBox="0 0 44 40" fill="none" stroke="#1e8fd6" stroke-width="3" stroke-linecap="round" stroke-linejoin="round"><path d="M12 18 a11 11 0 0 1 19 -8"/><path d="M31 4 v7 h-7"/><path d="M32 18 a11 11 0 0 1 -13 10"/><path d="M3 30 L12 26 L22 28 L34 24 L38 27 L26 36 L8 36 Z"/></svg>
      </span>
      <span class="benefit-text"><span class="no">No</span> Loss of Ownership</span>
    </li>
  </ul>

  <p class="payout">Receive cash by lump<br>sum, monthly installments<br>or a line of credit!!</p>

  <section class="consult-band"><span class="notch"></span></section>
  <div class="gallery-photo one" role="img" aria-label="Thoughtful senior man resting his chin on his hands"></div>
  <div class="gallery-photo two" role="img" aria-label="Happy senior couple sitting in a convertible car"></div>
  <div class="gallery-photo three" role="img" aria-label="Senior woman looking at her mobile phone at home"></div>
  <h2 class="consult-title">FOR A FREE CONSULTATION!!</h2>

  <section class="layer contact">
    <svg class="phone-icon" width="68" height="118" viewBox="0 0 68 118" fill="none" stroke="#9dca3a" stroke-width="5"><rect x="3" y="3" width="62" height="112" rx="8"/><line x1="3" y1="16" x2="65" y2="16"/><line x1="3" y1="98" x2="65" y2="98"/><line x1="28" y1="107" x2="40" y2="107" stroke-linecap="round"/></svg>
    <p class="call-label">CALL US TODAY</p>
    <p class="call-number">(800) 471-2965</p>
    <p class="company-line">
      <svg width="22" height="28" viewBox="0 0 22 28"><path d="M11 1 C5 1 1 5.5 1 11 C1 18 11 27 11 27 C11 27 21 18 21 11 C21 5.5 17 1 11 1 Z" fill="#0b5c87"/><circle cx="11" cy="11" r="4" fill="#fff"/></svg>
      <span>BLUEGATE FINANCIAL SERVICES, INC. NMLS #318760</span>
    </p>
    <p class="web-button">
      <svg width="28" height="28" viewBox="0 0 28 28" fill="none" stroke="#fff" stroke-width="2"><circle cx="14" cy="14" r="12"/><ellipse cx="14" cy="14" rx="5.5" ry="12"/><line x1="2" y1="14" x2="26" y2="14"/><line x1="4" y1="8" x2="24" y2="8"/><line x1="4" y1="20" x2="24" y2="20"/></svg>
      <span>WWW.BLUEGATEHOME.COM</span>
    </p>
  </section>
</main>
</body>
</html>
```